Business Card Design Project

Please refer to this project for further instructions: http://jobs.pixelvantor.com/job.aspx?id=218905

Industry/Entity Type

Business

```html
<!DOCTYPE html>
<html lang="en">
<head>
<meta charset="UTF-8">
<title>Nearwise – Business Card</title>
<link rel="stylesheet" href="https://fonts.googleapis.com/css2?family=Roboto+Condensed:wght@700&display=swap">
<style>
  :root {
    --paper: #ffffff;
    --leaf-light: #8cc63f;
    --leaf-mid: #5fa83a;
    --leaf-dark: #0a6b38;
    --edge-green: #3d8c2f;
    --brand-green: #2f8a34;
    --ink-light: #ffffff;
  }
  html, body {
    margin: 0;
    padding: 0;
    overflow: hidden;
    background: var(--paper);
  }
  .card {
    position: relative;
    width: 1200px;
    height: 686px;
    overflow: hidden;
    background: var(--paper);
    font-family: "Roboto Condensed", "Arial Narrow", sans-serif;
    font-weight: 700;
  }
  .card-backdrop {
    position: absolute;
    inset: 0;
    width: 1200px;
    height: 686px;
  }
  .brand-block {
    position: absolute;
    left: 60px;
    top: 228px;
    width: 440px;
    height: 120px;
    display: flex;
    align-items: center;
    justify-content: center;
    gap: 22px;
  }
  .brand-dot {
    width: 92px;
    height: 92px;
    border-radius: 50%;
    background: var(--brand-green);
    flex: none;
  }
  .brand-name {
    color: var(--brand-green);
    font-size: 66px;
    letter-spacing: 1px;
    line-height: 1;
  }
  .holder-title {
    position: absolute;
    left: 611px;
    top: 112px;
    margin: 0;
    color: var(--ink-light);
    font-size: 48px;
    line-height: 1;
    letter-spacing: 0.5px;
  }
  .contact-list {
    position: absolute;
    left: 611px;
    top: 380px;
    margin: 0;
    padding: 0;
    list-style: none;
    color: var(--ink-light);
    font-size: 48px;
    line-height: 66px;
    letter-spacing: 0.5px;
  }
</style>
</head>
<body>
  <div class="card">
    <svg class="card-backdrop" viewBox="0 0 1200 686" aria-hidden="true">
      <defs>
        <linearGradient id="leafSweep" x1="0" y1="0" x2="1" y2="0">
          <stop offset="0" stop-color="var(--leaf-light)"/>
          <stop offset="0.45" stop-color="var(--leaf-mid)"/>
          <stop offset="1" stop-color="var(--leaf-dark)"/>
        </linearGradient>
      </defs>
      <path class="edge-band" d="M372 0 Q742 343 372 686 L1200 686 L1200 0 Z" fill="var(--edge-green)"/>
      <path class="green-panel" d="M394 0 Q764 343 394 686 L1200 686 L1200 0 Z" fill="url(#leafSweep)"/>
    </svg>

    <div class="brand-block">
      <span class="brand-dot"></span>
      <span class="brand-name">NEARWISE</span>
    </div>

    <h1 class="holder-title">NEARWISE - Owner</h1>

    <ul class="contact-list">
      <li class="contact-phone">M - 555-555-5555</li>
      <li class="contact-email">E - hello@nearwise.com</li>
      <li class="contact-web">W - www.nearwise.com</li>
    </ul>
  </div>
</body>
</html>
```